Webdesign für Bedrucken Papiertaschen, Schildern etc.
Zielgruppe
Wir bedrucken Papiertaschen, Papierbeutel, Laternen, Aluplaketten, Schilder, etc. und lasern Hundemarken. Zielgruppen von Privat bis Geschäftskunden
Aufgabenstellung
Der Shop sollte ein einfacher und kostengünstiger 'web2print'-shop werden. Wo die Kunden anhand von einem Editor Ihre Logos oder Druckvorlagen selber hochladen und/oder gestalten könne. Bisher haben die Kunden eifach ihre Bidldatei per E-Mail geschickt und wir haben diese dann weiter verarbeit.
Der Shop sollte, wenn möglich, günstig im Unterhalt sein, da wir nicht abschätzen können, wie gut diese laufen wird.
Wir haben wie 3 Bereich: 1. Papierbeutel/Taschen / 2. Stallplaketten (für z.B. Pferdesport) / 3. Diverses (Wie z.B. die Laternen, Schilder, Hundemarken, etc.)
Es würde sich um eine separate Webseite handeln. Daher ist bei Design freie Hand, eifach und klar... auch für nicht so ambitionierte Privatkunden oder kleine Unternehmen.

```html
<!DOCTYPE html>
<html lang="de">
<head>
<meta charset="utf-8">
<title>Nordwerk Print – Web2Print Shop</title>
<link href="https://fonts.googleapis.com/css2?family=Inter:wght@400;500;600;700;800&display=swap" rel="stylesheet">
<style>
:root{
  --ink:#0b0b0b;
  --slate:#3a4556;
  --muted:#4a4f57;
  --blue:#1a9be6;
  --grey-bg:#ebebeb;
  --line:#e3e3e3;
  --chip:#ececec;
  --white:#fff;
}
*{box-sizing:border-box;margin:0;padding:0}
html,body{width:1200px;height:2241px;overflow:hidden;background:var(--white);font-family:"Inter",sans-serif;color:var(--ink)}
.page{position:relative;width:1200px;height:2241px}
.abs{position:absolute}
/* header */
.header{left:52px;top:0;width:1095px;height:96px;background:#fff;border-radius:0 0 18px 18px;box-shadow:0 6px 18px rgba(0,0,0,.12)}
.brand{left:24px;top:34px;font-weight:800;font-size:20px;letter-spacing:-.5px;display:flex;align-items:center;gap:8px}
.brand .sq{width:16px;height:16px;background:var(--ink)}
.nav{left:148px;top:41px;display:flex;gap:37px;font-size:12px;color:#333}
.nav .active{text-decoration:underline;color:var(--ink)}
.tools{right:20px;top:28px;display:flex;gap:13px}
.tool{width:45px;height:45px;border:1px solid #ddd;border-radius:8px;display:flex;align-items:center;justify-content:center}
.tool.dark{background:var(--ink);border-color:var(--ink)}
/* hero */
.eyebrow{font-size:11px;font-weight:600;letter-spacing:2.4px}
.hero-title{left:74px;top:228px;font-size:54px;font-weight:800;line-height:63px;letter-spacing:-.5px}
.hero-text{left:74px;top:378px;font-size:15px;line-height:25px;color:#222}
.btn{display:flex;align-items:center;justify-content:center;border-radius:5px;font-size:13px;font-weight:500}
.btn-blue{background:var(--blue);color:#fff}
.btn-outline{border:1.5px solid var(--ink);color:var(--ink)}
/* headings */
.h2{font-size:31px;font-weight:700;color:var(--slate);letter-spacing:-.3px}
.sub{font-size:15px;color:#444}
/* category cards */
.cat{top:751px;width:328px;height:278px;border:1px solid var(--line);border-top:4px solid var(--slate);border-radius:8px;background:#fff}
.icon-circle{width:65px;height:65px;border-radius:50%;background:radial-gradient(circle at 40% 30%,#3a3a3a,#0b0b0b);display:flex;align-items:center;justify-content:center}
.cat .icon-circle{position:absolute;left:26px;top:26px}
.chip{background:var(--chip);border-radius:12px;font-size:10px;padding:5px 9px;color:#222}
.cat .chip{position:absolute;left:111px;top:50px}
.cat h3{position:absolute;left:26px;top:116px;font-size:19px;font-weight:700;color:var(--slate)}
.cat p{position:absolute;left:26px;top:148px;width:285px;font-size:11.5px;line-height:18px;color:#444}
.cat .btn{position:absolute;left:26px;top:211px;width:145px;height:36px;font-size:12px}
/* steps */
.steps{left:8px;top:1090px;width:1184px;height:341px;background:var(--grey-bg)}
.step{top:1220px;width:342px}
.step .icon-circle{position:absolute;left:0;top:0}
.num{position:absolute;left:53px;top:-2px;width:26px;height:26px;border-radius:50%;background:#fff;font-size:17px;display:flex;align-items:center;justify-content:center}
.step .rule{position:absolute;left:79px;top:33px;right:0;height:1.5px;background:var(--slate)}
.step h3{position:absolute;left:0;top:92px;font-size:19px;font-weight:700;color:var(--slate);white-space:nowrap}
.step p{position:absolute;left:0;top:119px;width:300px;font-size:15px;line-height:25px;color:#444}
/* products */
.prod{top:1570px;width:238px;height:281px;border:1px solid var(--line);border-radius:6px;background:#fff}
.prod .img{position:absolute;left:7px;top:8px;width:222px;height:138px;border-radius:6px;background:radial-gradient(ellipse 30% 50% at 50% 52%,#b98a52 0%,#8a6236 55%,#0b0b0b 100%)}
.prod .chip{position:absolute;left:7px;top:168px;font-size:9.5px;padding:4px 9px}
.prod h4{position:absolute;left:7px;top:200px;width:220px;font-size:13.5px;font-weight:600;line-height:16px;color:var(--slate)}
.plus{position:absolute;right:9px;bottom:11px;width:32px;height:32px;border-radius:5px;background:var(--blue);display:flex;align-items:center;justify-content:center}
/* footer */
.footer{left:8px;top:1929px;width:1184px;height:303px;background:var(--ink);color:#fff}
.foot-brand{left:66px;top:52px;font-size:26px;font-weight:800;display:flex;align-items:center;gap:10px}
.foot-brand .sq{width:20px;height:20px;background:#fff}
.addr{left:249px;top:52px;font-size:15px;line-height:25px}
.addr b{font-weight:600}
.contact{left:249px;display:flex;align-items:center;gap:4px;font-size:15px;font-weight:600}
.pill{background:#fff;color:var(--ink);border-radius:16px;padding:5px 11px;font-weight:400}
.links{left:608px;top:75px;display:flex;flex-direction:column;gap:9px;font-size:15px}
.links a{color:#fff}
.cert{left:993px;top:91px;width:124px;height:124px;border-radius:50%;background:#fff;border:4px dashed #ddd}
.copy{left:66px;top:268px;font-size:15px}
</style>
</head>
<body>
<div class="page">

  <header class="abs header">
    <div class="abs brand"><span class="sq"></span>Nordwerk</div>
    <nav class="abs nav">
      <span class="active">Produkte</span><span>Sonderanfertigung</span><span>Aktionen</span><span>Materialien</span><span>Nachhaltigkeit</span><span>Über uns</span><span>Kontakt</span>
    </nav>
    <div class="abs tools">
      <div class="tool"><svg width="18" height="18" viewBox="0 0 24 24" fill="none" stroke="#111" stroke-width="1.6"><circle cx="12" cy="8" r="4"/><path d="M4 21c1-5 4-7 8-7s7 2 8 7"/></svg></div>
      <div class="tool"><svg width="18" height="18" viewBox="0 0 24 24" fill="none" stroke="#111" stroke-width="1.6"><path d="M12 20s-8-5-8-11a4.5 4.5 0 0 1 8-2.5A4.5 4.5 0 0 1 20 9c0 6-8 11-8 11z"/></svg></div>
      <div class="tool"><svg width="18" height="18" viewBox="0 0 24 24" fill="none" stroke="#111" stroke-width="1.6"><circle cx="11" cy="11" r="7"/><path d="M16 16l5 5"/></svg></div>
      <div class="tool dark"><svg width="20" height="20" viewBox="0 0 24 24" fill="none" stroke="#fff" stroke-width="1.6"><path d="M3 9h18l-2 11H5z"/><path d="M8 9l4-5 4 5M9 13v4M12 13v4M15 13v4"/></svg></div>
    </div>
  </header>

  <div class="abs eyebrow" style="left:74px;top:199px">WEB2PRINT SHOP</div>
  <h1 class="abs hero-title">Ihre Marke.<br>Perfekt gedruckt.</h1>
  <p class="abs hero-text">Gestalten Sie individuelle Papierbeutel, Stallplaketten und<br>Werbemittel – einfach online, direkt druckfertig.</p>
  <div class="abs btn btn-blue" style="left:74px;top:446px;width:181px;height:42px">Jetzt gestalten →</div>
  <div class="abs btn btn-outline" style="left:268px;top:446px;width:156px;height:42px">Alle Produkte</div>

  <svg class="abs" style="left:583px;top:141px" width="456" height="444" viewBox="0 0 456 444" role="img" aria-label="Foto: Person in Bewegung mit braunen Papiertaschen">
    <defs>
      <linearGradient id="heroGrad" x1="0" y1="0" x2="1" y2="1">
        <stop offset="0" stop-color="#d9cdb8"/>
        <stop offset=".35" stop-color="#d4a02a"/>
        <stop offset=".7" stop-color="#7a5a3a"/>
        <stop offset="1" stop-color="#4a3a2c"/>
      </linearGradient>
    </defs>
    <path d="M205 0C290 0 360 60 410 150C450 220 470 300 445 360C420 420 360 444 280 444C180 444 80 420 30 360C-10 310-5 250 20 190C60 90 120 0 205 0Z" fill="url(#heroGrad)"/>
  </svg>

  <div class="abs eyebrow" style="left:74px;top:637px">KATEGORIEN</div>
  <h2 class="abs h2" style="left:74px;top:665px">Was möchten Sie gestalten?</h2>
  <p class="abs sub" style="left:74px;top:712px">Wählen Sie Ihre Kategorie und starten Sie direkt mit dem Design</p>

  <div class="abs cat" style="left:74px">
    <div class="icon-circle"><svg width="28" height="28" viewBox="0 0 24 24" fill="none" stroke="#fff" stroke-width="1.5"><rect x="4" y="4" width="16" height="16" rx="3"/><path d="M9 7v2a3 3 0 0 0 6 0V7"/></svg></div>
    <span class="chip">45+ Produkte</span>
    <h3>Papierbeutel &amp; Taschen</h3>
    <p>Tragetaschen, Papierbeutel, Flachbeutel mit Ihrem Logo – in vielen Formaten und Materialien.</p>
    <div class="btn btn-blue">Jetzt entdecken →</div>
  </div>
  <div class="abs cat" style="left:436px">
    <div class="icon-circle"><svg width="28" height="28" viewBox="0 0 24 24" fill="none" stroke="#fff" stroke-width="1.5"><path d="M7 4h10v5a5 5 0 0 1-10 0z"/><path d="M7 6H4a3 3 0 0 0 3 4M17 6h3a3 3 0 0 1-3 4M12 14v4M8 20h8"/></svg></div>
    <span class="chip">25+ Produkte</span>
    <h3>Stahlplaketten</h3>
    <p>Individuell gravierte Plaketten für Pferdesport, Turniere und Vereinsauszeichnungen.</p>
    <div class="btn btn-blue">Jetzt entdecken →</div>
  </div>
  <div class="abs cat" style="left:798px">
    <div class="icon-circle"><svg width="28" height="28" viewBox="0 0 24 24" fill="none" stroke="#fff" stroke-width="1.5"><path d="M6 9h12v11H6z"/><path d="M9 9V6a3 3 0 0 1 6 0v3"/></svg></div>
    <span class="chip">45+ Produkte</span>
    <h3>Diverses</h3>
    <p>Laternen, Schilder, Hundemarken, Schlüsselanhänger und viele weitere Werbeartikel.</p>
    <div class="btn btn-blue">Jetzt entdecken →</div>
  </div>

  <div class="abs steps"></div>
  <div class="abs eyebrow" style="left:74px;top:1135px">SO FUNKTIONIERT'S</div>
  <h2 class="abs h2" style="left:74px;top:1158px">In 3 Schritten zum fertigen Druckprodukt</h2>

  <div class="abs step" style="left:74px">
    <div class="icon-circle"><svg width="28" height="28" viewBox="0 0 24 24" fill="none" stroke="#fff" stroke-width="1.5"><rect x="4" y="4" width="16" height="16" rx="3"/><path d="M9 7v2a3 3 0 0 0 6 0V7"/></svg></div>
    <span class="num">1</span><span class="rule"></span>
    <h3>Produkt wählen</h3>
    <p>Wählen Sie aus über 120 Produkten das passende für Ihren Bedarf.</p>
  </div>
  <div class="abs step" style="left:436px">
    <div class="icon-circle"><svg width="28" height="28" viewBox="0 0 24 24" fill="none" stroke="#fff" stroke-width="1.5"><path d="M8 13a4 4 0 1 1 8 0c0 2-2 3-2 5h-4c0-2-2-3-2-5z"/><path d="M10 21h4M12 3v2M5 6l1.5 1.5M19 6l-1.5 1.5M3 13h2M19 13h2"/></svg></div>
    <span class="num">2</span><span class="rule"></span>
    <h3>Motiv gestalten</h3>
    <p>Laden Sie Ihr Logo hoch oder nutzen Sie unseren Editor für individuelle Designs.</p>
  </div>
  <div class="abs step" style="left:798px">
    <div class="icon-circle"><svg width="28" height="28" viewBox="0 0 24 24" fill="none" stroke="#fff" stroke-width="1.5"><path d="M12 3l8 4v8l-8 4-8-4V7z"/><path d="M4 7l8 4 8-4M12 11v8M14 17l2 2 4-4"/></svg></div>
    <span class="num">3</span><span class="rule"></span>
    <h3>Bestellen &amp; liefern</h3>
    <p>Bestellung abschicken und Ihr fertiges Produkt kommt direkt zu Ihnen.</p>
  </div>

  <h2 class="abs h2" style="left:74px;top:1491px">Beliebte Produkte</h2>
  <p class="abs sub" style="left:74px;top:1539px">Unsere meistbestellten Artikel</p>

  <div class="abs prod" style="left:74px"><div class="img" role="img" aria-label="Produktfoto: braune Papiertasche mit Aufdruck"></div><span class="chip">Papierbeutel &amp; Taschen</span><h4>Papiertaschen braun (2-seitig bedruckt)</h4><div class="plus"><svg width="16" height="16" viewBox="0 0 16 16" stroke="#fff" stroke-width="2"><path d="M8 2v12M2 8h12"/></svg></div></div>
  <div class="abs prod" style="left:345px"><div class="img" role="img" aria-label="Produktfoto: braune Papiertasche mit Aufdruck"></div><span class="chip">Papierbeutel &amp; Taschen</span><h4>Papiertaschen braun (2-seitig bedruckt)</h4><div class="plus"><svg width="16" height="16" viewBox="0 0 16 16" stroke="#fff" stroke-width="2"><path d="M8 2v12M2 8h12"/></svg></div></div>
  <div class="abs prod" style="left:615px"><div class="img" role="img" aria-label="Produktfoto: braune Papiertasche mit Aufdruck"></div><span class="chip">Papierbeutel &amp; Taschen</span><h4>Papiertaschen braun (2-seitig bedruckt)</h4><div class="plus"><svg width="16" height="16" viewBox="0 0 16 16" stroke="#fff" stroke-width="2"><path d="M8 2v12M2 8h12"/></svg></div></div>
  <div class="abs prod" style="left:886px"><div class="img" role="img" aria-label="Produktfoto: braune Papiertasche mit Aufdruck"></div><span class="chip">Papierbeutel &amp; Taschen</span><h4>Papiertaschen braun (2-seitig bedruckt)</h4><div class="plus"><svg width="16" height="16" viewBox="0 0 16 16" stroke="#fff" stroke-width="2"><path d="M8 2v12M2 8h12"/></svg></div></div>

  <footer class="abs footer">
    <div class="abs foot-brand"><span class="sq"></span>Nordwerk</div>
    <div class="abs addr"><b>Nordwerk Print AG</b><br>Werkstrasse 14<br>CH-8000 Musterdorf / Zürich</div>
    <div class="abs contact" style="top:137px">T: <span class="pill">044 000 12 34</span></div>
    <div class="abs contact" style="top:182px">E: <span class="pill">info@nordwerk-print.ch</span></div>
    <div class="abs links">
      <a href="#">Versandbedingungen</a>
      <a href="#">Allgemeine Geschäftsbedingungen</a>
      <a href="#">Widerrufsrecht</a>
      <a href="#">Datenschutz</a>
      <a href="#">Impressum</a>
    </div>
    <div class="abs cert"></div>
    <div class="abs copy">© Nordwerk Print AG 2026</div>
  </footer>

</div>
</body>
</html>
```